Mexican construction company needs a business card design

We need a business card design for a company based in Monterrey, Mexico called:

Desarrollos Quilbeta S.A. de C.V.

The company is in the construction business and I would like the businees card to be simple and concise. Please use white background and blue or black text color that say:

"Proyectos de Construcción"-- (Brief description of business)
" Rodrigo Velun Osorio"--- (My name)
"rvelun@correoplat.mx"-- (My email)
"C: (81) 52 19 67 43"-- (My cell)
"O: (81) 56 72 18 94"-- (Office phone)

Please use only the colors of my company that are attached

Please make the back of the business card blue (same blue from logo) and use the logo.

Thanks!

```html
<!DOCTYPE html>
<html lang="es">
<head>
<meta charset="utf-8">
<title>Desarrollos Quilbeta – Tarjeta de presentación</title>
<link rel="stylesheet" href="https://fonts.googleapis.com/css2?family=Lato:wght@400;700;900&display=swap">
<style>
  :root {
    --navy: #14125a;
    --grey: #9a9ca1;
    --paper: #ffffff;
    --label: #9a9ca1;
    --stage: #e6e4df;
  }
  * { margin: 0; padding: 0; box-sizing: border-box; }
  html, body { width: 1200px; height: 899px; overflow: hidden; }
  body {
    background: var(--stage);
    font-family: "Lato", sans-serif;
    position: relative;
  }
  .card {
    position: absolute;
    left: 320px;
    width: 560px;
    height: 320px;
    overflow: hidden;
    box-shadow: 0 6px 18px rgba(0,0,0,.18);
  }
  .card--back { top: 80px; background: var(--navy); }
  .card--front { top: 490px; background: var(--paper); }

  .wordmark {
    color: var(--paper);
    font-weight: 900;
    text-transform: uppercase;
    line-height: 1;
  }
  .card--back .wordmark {
    position: absolute;
    left: 0; right: 0; top: 128px;
    text-align: center;
  }
  .wordmark__top { display: block; font-size: 15px; letter-spacing: 3px; }
  .wordmark__main { display: block; font-size: 31px; letter-spacing: 5px; margin-top: 4px; }

  .corner { position: absolute; top: 0; right: 0; }

  .brand {
    position: absolute;
    left: 40px; top: 58px;
    display: flex; align-items: center; gap: 12px;
  }
  .brand__square { width: 34px; height: 34px; background: var(--grey); }
  .brand .wordmark { color: var(--navy); }
  .brand .wordmark__top { font-size: 12px; letter-spacing: 2.5px; }
  .brand .wordmark__main { font-size: 24px; letter-spacing: 4px; margin-top: 3px; }

  .person {
    position: absolute;
    left: 40px; top: 128px;
    color: var(--navy);
  }
  .person__name {
    font-size: 17px; font-weight: 700;
    letter-spacing: 1px; text-transform: uppercase;
    margin-bottom: 12px;
  }
  .contact { list-style: none; font-size: 14px; line-height: 1.5; }
  .contact__label { color: var(--label); font-size: 11px; display: inline-block; width: 46px; }

  .tagline-band {
    position: absolute;
    left: 0; right: 0; bottom: 0;
    height: 40px;
    background: var(--navy);
    color: var(--paper);
    display: flex; align-items: center; justify-content: flex-end;
    padding-right: 36px;
    font-size: 12px; letter-spacing: 3px; text-transform: uppercase;
  }
</style>
</head>
<body>
  <section class="card card--back" aria-label="Reverso de la tarjeta">
    <div class="wordmark">
      <span class="wordmark__top">Desarrollos</span>
      <span class="wordmark__main">Quilbeta</span>
    </div>
  </section>

  <section class="card card--front" aria-label="Frente de la tarjeta">
    <svg class="corner" width="200" height="160" viewBox="0 0 200 160" aria-hidden="true">
      <polygon points="90,0 200,0 200,110" fill="var(--navy)"/>
    </svg>

    <div class="brand">
      <span class="brand__square"></span>
      <div class="wordmark">
        <span class="wordmark__top">Desarrollos</span>
        <span class="wordmark__main">Quilbeta</span>
      </div>
    </div>

    <div class="person">
      <p class="person__name">Rodrigo Velun Osorio</p>
      <ul class="contact">
        <li><span class="contact__label">Cell</span>(81) 52 19 67 43</li>
        <li><span class="contact__label">Office</span>(81) 56 72 18 94</li>
        <li><span class="contact__label">E-mail</span>rvelun@correoplat.mx</li>
      </ul>
    </div>

    <div class="tagline-band">Proyectos de Construcción</div>
  </section>
</body>
</html>
```